Business Card Design Project

I am a Chiropractor that is looking for a new business card.  Our logo was slightly changed lately, therefore need a new, more professional look.
We are a modern, non-stuffy chiropractic office.  Want a contemporary look that will let people know this is not your typical doctors office.  Our logo is red, and contains the name of our business: realign.  The u in the logo is green, stressing the most important part of our business: "u"

Target Market(s)
moderate to upper income bracket, family friendly
www.realignspine-example.com
Gordon Pell
Family Chiropractor
314 Hollis Rd
Millbrook, NM 87999
512.555.0147 phone
512.555.0148 fax
Industry/Entity Type
Business
Requirements
Must have
- www.realignspine-example.com
Gordon Pell
Family Chiropractor
314 Hollis Rd
Millbrook, NM 87999
512.555.0147 phone
512.555.0148 fax

```html
<!DOCTYPE html>
<html lang="en">
<head>
<meta charset="utf-8">
<title>realign — Business Card</title>
<link rel="stylesheet" href="https://fonts.googleapis.com/css2?family=Mulish:wght@400;700&display=swap">
<style>
  :root {
    --page-bg: #ffffff;
    --card-bg: #f4f4f4;
    --card-edge: #e2e2e2;
    --brand-red: #e8413a;
    --brand-green: #6cbf3a;
    --text-grey: #5c5c5c;
  }
  html, body {
    margin: 0;
    padding: 0;
    width: 1200px;
    height: 900px;
    overflow: hidden;
    background: var(--page-bg);
  }
  .canvas {
    position: relative;
    width: 1200px;
    height: 900px;
    font-family: "Mulish", "Century Gothic", sans-serif;
  }
  .business-card {
    position: absolute;
    left: 210px;
    top: 174px;
    width: 760px;
    height: 430px;
    border-radius: 30px;
    background: var(--card-bg);
    border: 1px solid var(--card-edge);
  }
  .brand-name {
    position: absolute;
    left: 74px;
    top: 68px;
    margin: 0;
    font-size: 80px;
    font-weight: 400;
    line-height: 1;
    letter-spacing: 1px;
    color: var(--brand-red);
  }
  .website {
    position: absolute;
    left: 72px;
    top: 222px;
    margin: 0;
    font-size: 20px;
    line-height: 24px;
    color: var(--brand-green);
  }
  .contact-block {
    position: absolute;
    left: 464px;
    top: 206px;
  }
  .person-name {
    margin: 0;
    font-size: 30px;
    font-weight: 700;
    text-transform: uppercase;
    letter-spacing: 0.5px;
    line-height: 36px;
    color: var(--brand-red);
  }
  .person-title {
    margin: 0 0 8px;
    font-size: 22px;
    line-height: 30px;
    color: var(--brand-green);
  }
  .address, .phones {
    margin: 0;
    font-size: 22px;
    line-height: 28px;
    color: var(--text-grey);
    font-style: normal;
  }
  .address { margin-bottom: 8px; }
</style>
</head>
<body>
<div class="canvas">
  <section class="business-card">
    <p class="brand-name">realign</p>
    <p class="website">www.realignspine-example.com</p>
    <div class="contact-block">
      <p class="person-name">Gordon Pell</p>
      <p class="person-title">Family Chiropractor</p>
      <address class="address">314 Hollis Rd<br>Millbrook, NM 87999</address>
      <p class="phones">512.555.0147 phone<br>512.555.0148 fax</p>
    </div>
  </section>
</div>
</body>
</html>
```